Tarnwick Sprouts Presents Dr Cora Villant from Grainfield Labs of Tolvern

Tarnwick Sprouts is bringing Dr Cora Villant from Grainfield Labs of Tolvern to Auckland for a one day only seminar. Dr Villant is recognised as a world authority on turfgrass. Cora received her master's and Ph.D from the Halvers College where she first worked on heat tolerant bentgrasses and improved bermuda grasses. Cora's work reflects the Harvest of Notions approach that drives product development. At Grainfield Labs of Tolvern, our emphasis is on producing grasses that can survive with less water, and are highly disease resistance, reducing or eliminating the need for fungicides and fertilizers. By interacting with superintendents and distributors, we determine their needs and then find solutions to satisfy the requirements of their projects.

Target Market(s)

Turf managers in New Zealand

Font styles to use
Serif

Colors

Designer to choose colors to be used in the design.

Requirements
Must have
• Date: Friday 31 August 2018 at Quaymont Lodge Terminal, 10.30am until 3pm
• Morning tea served from 9.30am
• Free parking in Carpark A
• Please let us know if you have any special dietary requirements
Nice to have
• All three logos, above information about Cora

```html
<!DOCTYPE html>
<html lang="en">
<head>
<meta charset="utf-8">
<title>Tarnwick Sprouts Seminar Flyer</title>
<link href="https://fonts.googleapis.com/css2?family=PT+Serif:wght@400;700&display=swap" rel="stylesheet">
<style>
  :root {
    --backdrop: #1c1f24;
    --paper: #ffffff;
    --turf-green: #1d5a2e;
    --turf-green-dark: #154524;
    --ink: #2b2b2b;
    --accent-red: #b3202a;
    --photo-sky: #b9c6d6;
    --photo-grass: #4f7d2c;
  }
  * { margin: 0; padding: 0; box-sizing: border-box; }
  html, body { width: 1200px; height: 848px; overflow: hidden; background: var(--backdrop); }
  .canvas { width: 1200px; height: 848px; display: flex; align-items: center; justify-content: center; }
  .flyer {
    width: 600px; height: 848px; background: var(--paper);
    display: flex; flex-direction: column; font-family: "PT Serif", serif;
  }
  .hero-photo {
    flex: none; height: 296px;
    background: linear-gradient(180deg, var(--photo-sky) 0%, #d6dde6 45%, #8aa36a 70%, var(--photo-grass) 100%);
  }
  .intro-band {
    flex: none;
    background: var(--turf-green);
    color: var(--paper);
    padding: 18px 32px 20px;
    font-size: 13px; line-height: 1.45; font-weight: 700;
    text-align: justify;
  }
  .details {
    flex: 1; min-height: 0; display: flex; padding: 16px 28px 14px; gap: 20px;
  }
  .sponsors { width: 214px; flex: none; display: flex; flex-direction: column; gap: 16px; justify-content: center; }
  .sponsor { display: flex; align-items: center; gap: 10px; font-weight: 700; }
  .sponsor-mark { width: 40px; height: 40px; border-radius: 50%; background: var(--turf-green); flex: none; }
  .sponsor-name { font-size: 17px; line-height: 1.2; color: var(--turf-green); }
  .sponsor-name--red { color: var(--accent-red); }
  .sponsor-name--ink { color: var(--ink); }
  .event-info { flex: 1; display: flex; flex-direction: column; gap: 9px; justify-content: center; }
  .info-box {
    border: 2px solid var(--ink);
    padding: 6px 12px;
    font-weight: 700;
    font-size: 15px; line-height: 1.25; color: var(--ink);
  }
  .footer-strip { flex: none; height: 30px; background: linear-gradient(180deg, var(--turf-green), var(--turf-green-dark)); }
</style>
</head>
<body>
<div class="canvas">
  <article class="flyer">
    <div class="hero-photo" role="img" aria-label="Photo of Dr Cora Villant holding potted turfgrass inside a greenhouse"></div>
    <section class="intro-band">
      Dr Villant is recognised as a world authority on turfgrass. Cora received her master's and Ph.D from the Halvers College where she first worked on heat tolerant bentgrasses and improved bermuda grasses. Cora's work reflects the Harvest of Notions approach that drives product development. At Grainfield Labs of Tolvern, our emphasis is on producing grasses that can survive with less water, and are highly disease resistance, reducing or eliminating the need for fungicides and fertilizers. By interacting with superintendents and distributors, we determine their needs and then find solutions to satisfy the requirements of their projects.
    </section>
    <section class="details">
      <div class="sponsors">
        <div class="sponsor"><span class="sponsor-mark"></span><span class="sponsor-name">Tarnwick Sprouts</span></div>
        <div class="sponsor"><span class="sponsor-name sponsor-name--ink">Korvel Seeds &amp; Science</span></div>
        <div class="sponsor"><span class="sponsor-name sponsor-name--red">Grainfield Labs of Tolvern</span></div>
      </div>
      <div class="event-info">
        <p class="info-box">Friday 31 August 2018 at Quaymont Lodge Terminal, 10.30am until 3pm</p>
        <p class="info-box">Morning Tea Served from 9.30am</p>
        <p class="info-box">Free parking in Carpark A</p>
        <p class="info-box">Please let us know if you have any special dietary requirements</p>
      </div>
    </section>
    <div class="footer-strip"></div>
  </article>
</div>
</body>
</html>
```